App for our juice bar

We need an app for our juice bar. We would like to implement a customer loyalty program as well as the ability for our customers to order on the app.

Colors
6b449b
f37122
9ccb3b
ffffff

Requirements
Must have
• Customer rewards capability. Customer ordering capability.

```html
<!DOCTYPE html>
<html lang="en">
<head>
<meta charset="utf-8">
<title>Swirl Juice Bar – App Screens</title>
<link href="https://fonts.googleapis.com/css2?family=Source+Sans+3:wght@300;400;600&display=swap" rel="stylesheet">
<style>
:root{
  --canvas:#ededed;
  --plum:#2e0435;
  --plum-deep:#23022a;
  --violet:#8a1690;
  --violet-soft:#9c2aa2;
  --orange:#fba11f;
  --white:#ffffff;
  --ink:#444;
}
*{box-sizing:border-box;margin:0;padding:0}
html,body{width:1200px;height:1200px;overflow:hidden;background:var(--canvas);font-family:"Source Sans 3",sans-serif;font-weight:300}
.canvas{position:relative;width:1200px;height:1200px}
h3{font-weight:300}

.brand{position:absolute;left:0;right:0;top:190px;display:flex;justify-content:center;align-items:center;gap:16px}
.brand-dot{width:46px;height:46px;border-radius:50%;background:var(--orange)}
.brand-name{font-size:56px;font-weight:600;color:var(--violet);letter-spacing:1px}
.brand-small{display:flex;align-items:center;gap:8px}
.brand-small .brand-dot{width:22px;height:22px}
.brand-small .brand-name{font-size:26px}

.screen{position:absolute;top:527px;width:296px;height:525px;overflow:hidden;background:var(--white)}
.screen-welcome{left:85px;background:var(--orange)}
.screen-menu{left:452px}
.screen-detail{left:819px;background:var(--plum-deep)}

.status{position:absolute;top:0;left:0;right:0;height:24px;display:flex;justify-content:space-between;align-items:center;padding:0 9px;font-size:7px;color:var(--white)}
.status-signal{letter-spacing:1px;font-weight:600}

/* welcome */
.welcome-top{position:absolute;left:0;top:0;width:296px;height:220px;background:var(--plum)}
.welcome-splash{position:absolute;left:0;top:220px;width:296px;height:125px;background:linear-gradient(180deg,var(--plum) 0%,#5a1f3a 55%,var(--orange) 100%)}
.skip{position:absolute;top:30px;right:11px;background:var(--violet);color:var(--white);font-size:9px;padding:3px 10px;border-radius:10px}
.welcome-brand{position:absolute;top:150px;left:0;right:0;justify-content:center}
.welcome-btn{position:absolute;left:31px;width:234px;height:41px;border-radius:21px;background:var(--violet);color:var(--orange);font-size:15px;display:flex;align-items:center;justify-content:center}
.btn-login{top:370px}
.btn-register{top:420px}
.welcome-note{position:absolute;left:28px;right:28px;bottom:16px;font-size:6px;line-height:1.35;color:var(--violet);text-align:center}

/* menu */
.screen-menu .status{background:var(--violet)}
.hero-photo{position:absolute;top:24px;left:0;width:296px;height:200px;background:linear-gradient(120deg,#f2f2f2 0%,#dedede 40%,#b7c96a 60%,#f7b733 85%,#f2f2f2 100%)}
.hero-dots{position:absolute;bottom:8px;left:0;right:0;display:flex;justify-content:center;gap:4px}
.hero-dots span{width:11px;height:11px;border-radius:50%;background:#cfc3d3}
.tabs{position:absolute;top:224px;left:0;width:296px;height:42px;display:flex;background:var(--violet)}
.tab{flex:1;display:flex;align-items:center;justify-content:center;font-size:11px;color:var(--plum)}
.tab-active{background:var(--violet-soft);color:var(--orange)}
.item{position:absolute;left:22px;width:260px;display:flex;gap:20px}
.item-1{top:288px}
.item-2{top:414px}
.item-photo{flex:none;width:108px;height:108px;border-radius:50%;border:7px solid var(--orange);background:linear-gradient(135deg,#f08a2a,#6f4a7f 55%,#3a2a40)}
.item-2 .item-photo{background:linear-gradient(135deg,#f6a233,#c84a1a)}
.item-body{padding-top:12px}
.item-title{font-size:11px;color:var(--violet)}
.item-text{font-size:7px;line-height:1.3;color:var(--ink);margin-top:5px;width:125px}
.order-pill{display:inline-block;margin-top:9px;background:var(--orange);color:var(--violet);font-size:11px;padding:4px 19px;border-radius:13px}
.nav{position:absolute;bottom:0;left:0;width:296px;height:63px;background:var(--violet);display:flex}
.nav-item{flex:1;display:flex;flex-direction:column;align-items:center;justify-content:center;gap:5px;font-size:11px;color:var(--white)}
.nav-item svg{width:20px;height:20px;fill:none;stroke:var(--white);stroke-width:1.4}

/* detail */
.screen-detail .status{opacity:.25}
.screen-detail .nav{background:#2a0a30;opacity:.5}
.dim-band{position:absolute;top:224px;left:0;width:296px;height:42px;background:#3d0c44}
.modal{position:absolute;top:80px;left:28px;width:241px;height:390px;background:var(--white)}
.modal-photo{height:182px;background:linear-gradient(120deg,#f2f2f2 0%,#dedede 40%,#b7c96a 60%,#f7b733 85%,#f2f2f2 100%)}
.modal-title{margin:16px 0 0 17px;font-size:14px;color:var(--violet)}
.modal-text{margin:8px 17px 0;font-size:10.5px;line-height:1.35;color:var(--ink)}
.modal-cta{position:absolute;left:0;right:0;bottom:0;height:47px;background:var(--violet);color:var(--white);font-size:14px;display:flex;align-items:center;justify-content:center}
.modal-close{position:absolute;top:72px;left:265px;width:25px;height:25px;border-radius:50%;background:var(--violet);color:var(--white);font-size:11px;display:flex;align-items:center;justify-content:center}
</style>
</head>
<body>
<div class="canvas">

  <div class="brand">
    <span class="brand-dot"></span>
    <span class="brand-name">Swirl Juice Bar</span>
  </div>

  <!-- Welcome screen -->
  <section class="screen screen-welcome">
    <div class="welcome-top"></div>
    <div class="welcome-splash" role="img" aria-label="Illustration of dark purple paint splashing into orange juice"></div>
    <div class="status"><span class="status-signal">•••••</span><span>12:00 PM</span></div>
    <div class="skip">Skip</div>
    <div class="brand brand-small welcome-brand">
      <span class="brand-dot"></span>
      <span class="brand-name" style="color:var(--orange)">Swirl Juice Bar</span>
    </div>
    <div class="welcome-btn btn-login">Login</div>
    <div class="welcome-btn btn-register">Register</div>
    <p class="welcome-note">Collect points with every juice you order and trade them for free drinks, seasonal blends and member treats. Sign in to see your rewards and order ahead from the nearest bar.</p>
  </section>

  <!-- Menu screen -->
  <section class="screen screen-menu">
    <div class="status"><span class="status-signal">•••••</span><span>12:00 PM</span></div>
    <div class="hero-photo" role="img" aria-label="Photo of a green smoothie cup with banana, orange and apple">
      <div class="hero-dots"><span></span><span></span><span></span><span></span><span></span></div>
    </div>
    <nav class="tabs">
      <div class="tab tab-active">BEST DEALS</div>
      <div class="tab">BEST FAV</div>
      <div class="tab">MIXMATCH</div>
    </nav>
    <article class="item item-1">
      <div class="item-photo" role="img" aria-label="Photo of a berry smoothie cup"></div>
      <div class="item-body">
        <h3 class="item-title">Juice 1</h3>
        <p class="item-text">Blended berries, banana and oat milk, poured fresh and ready to pick up.</p>
        <span class="order-pill">Order</span>
      </div>
    </article>
    <article class="item item-2">
      <div class="item-photo" role="img" aria-label="Photo of an orange juice"></div>
      <div class="item-body">
        <h3 class="item-title">Juice 2</h3>
        <p class="item-text">Orange, carrot and ginger</p>
      </div>
    </article>
    <nav class="nav">
      <div class="nav-item"><svg viewBox="0 0 20 20"><path d="M3 9L10 3L17 9V17H12V12H8V17H3Z"/></svg>Home</div>
      <div class="nav-item"><svg viewBox="0 0 20 20"><path d="M3 5H17M3 10H17M3 15H17"/></svg>Menu</div>
      <div class="nav-item"><svg viewBox="0 0 20 20"><path d="M10 2L12.4 7.2L18 7.8L13.8 11.5L15 17L10 14.2L5 17L6.2 11.5L2 7.8L7.6 7.2Z"/></svg>Promotion</div>
      <div class="nav-item"><svg viewBox="0 0 20 20"><circle cx="10" cy="7" r="4"/><path d="M3 18C3 13 17 13 17 18"/></svg>Account</div>
    </nav>
  </section>

  <!-- Detail screen -->
  <section class="screen screen-detail">
    <div class="status"><span class="status-signal">•••••</span><span>12:00 PM</span></div>
    <div class="dim-band"></div>
    <nav class="nav">
      <div class="nav-item"><svg viewBox="0 0 20 20"><path d="M3 9L10 3L17 9V17H12V12H8V17H3Z"/></svg>Home</div>
      <div class="nav-item"><svg viewBox="0 0 20 20"><path d="M3 5H17M3 10H17M3 15H17"/></svg>Menu</div>
      <div class="nav-item"><svg viewBox="0 0 20 20"><path d="M10 2L12.4 7.2L18 7.8L13.8 11.5L15 17L10 14.2L5 17L6.2 11.5L2 7.8L7.6 7.2Z"/></svg>Promotion</div>
      <div class="nav-item"><svg viewBox="0 0 20 20"><circle cx="10" cy="7" r="4"/><path d="M3 18C3 13 17 13 17 18"/></svg>Account</div>
    </nav>
    <div class="modal">
      <div class="modal-photo" role="img" aria-label="Photo of a green smoothie cup with banana, orange and apple"></div>
      <h3 class="modal-title">Juice</h3>
      <p class="modal-text">Lorem ipsum dolor sit amet, consectetur adipiscing elit, sed do eiusmod tempor incididunt ut labore et dolore magna aliqua. Ut enim ad minim veniam, quis nostrud exercitation ullamco laboris nisi ut aliquip ex ea commodo consequat. Duis aute irure dolor in</p>
      <div class="modal-cta">Order Now</div>
    </div>
    <div class="modal-close">X</div>
  </section>

</div>
</body>
</html>
```